Hollow Lantern Distillery

I need a label designed for my small distillery. I’d like it to have a rose, and the name hollow lantern in script writing. I need the graphic to fit a standard gin bottle and I’ll need to be able to edit it depending on alcohol, warning and descriptions. I want it to look elegant and attractive, but slightly daring too. It’s a 700ml oslo bottle
Target Market(s)
Bespoke gin and vodka drinkers
Industry/Entity Type
Beverage
Font styles to use
Script
Other font styles liked:
- Something easy to read
Requirements
Must have
- Room for me to add and remove text depending on the drink
Nice to have
- Hollow lantern in script, slight colour on the rose and black writing

```html
<!DOCTYPE html>
<html lang="en">
<head>
<meta charset="utf-8">
<title>Hollow Lantern – Gin Label</title>
<link href="https://fonts.googleapis.com/css2?family=Pinyon+Script&family=Montserrat:wght@500;600;700&family=Lora:ital@1&family=Arimo:wght@400;700&display=swap" rel="stylesheet">
<style>
  :root{
    --page:#ffffff;
    --label:#fbf9ec;
    --ink:#141414;
    --dim:#8a8a8a;
    --rose-light:#f6d3d6;
    --rose:#eaa8b0;
    --leaf:#6f8f5a;
    --leaf-dark:#3e5a35;
    --gold:#d9b26a;
  }
  *{box-sizing:border-box;margin:0;padding:0}
  html,body{width:694px;height:1200px;overflow:hidden;background:var(--page)}
  .canvas{position:relative;width:694px;height:1200px;color:var(--ink);font-family:"Montserrat",sans-serif}

  .dimension{position:absolute;color:var(--dim);font-family:"Arimo",sans-serif;font-size:13px}
  .dimension svg{position:absolute;left:0;top:0;overflow:visible}
  .dimension-label{position:absolute;white-space:nowrap}

  .label{position:absolute;background:var(--label);overflow:hidden}

  /* front */
  .label-front{left:76px;top:150px;width:549px;height:510px}
  .art-rose-main{position:absolute;left:0;top:0;width:310px;height:310px;
    background:radial-gradient(circle at 45% 25%,var(--rose-light) 0,var(--rose) 28%,rgba(111,143,90,.55) 52%,rgba(251,249,236,0) 72%)}
  .art-rose-side{position:absolute;right:-20px;top:320px;width:170px;height:150px;
    background:radial-gradient(circle at 55% 40%,var(--rose) 0,var(--rose-light) 30%,rgba(111,143,90,.45) 55%,rgba(251,249,236,0) 72%)}
  .art-leaves-base{position:absolute;right:40px;bottom:0;width:90px;height:30px;
    background:radial-gradient(ellipse at 50% 100%,rgba(62,90,53,.6),rgba(251,249,236,0) 70%)}
  .front-title{position:absolute;left:0;width:100%;text-align:center;font-family:"Pinyon Script",cursive;line-height:1}
  .front-title.line-1{top:120px;font-size:96px;padding-left:40px}
  .front-title.line-2{top:220px;font-size:96px;padding-left:20px}
  .front-batch{position:absolute;top:352px;left:0;width:100%;text-align:center;font-weight:700;font-size:22px;letter-spacing:5px}
  .front-badge{position:absolute;left:6px;top:290px;width:82px;height:82px;border-radius:50%;border:3px solid var(--gold);opacity:.8}
  .front-drink{position:absolute;top:382px;left:0;width:100%;text-align:center;font-family:"Pinyon Script",cursive;font-size:46px;padding-right:40px}
  .front-rule{position:absolute;top:432px;left:40px;width:390px;height:2px;background:var(--ink)}
  .front-specs{position:absolute;top:458px;left:40px;width:400px;display:flex;justify-content:space-between;align-items:baseline;font-weight:600;font-size:16px}
  .front-specs .volume{font-size:24px;font-weight:700}

  /* back */
  .label-back{left:185px;top:770px;width:294px;height:420px}
  .back-title{position:absolute;left:16px;top:20px;font-family:"Pinyon Script",cursive;font-size:30px;line-height:1;white-space:nowrap}
  .art-rose-back{position:absolute;right:2px;top:6px;width:70px;height:58px;
    background:radial-gradient(circle at 50% 45%,var(--rose) 0,var(--rose-light) 30%,rgba(111,143,90,.45) 55%,rgba(251,249,236,0) 72%)}
  .back-description{position:absolute;left:18px;top:78px;width:258px;text-align:center;font-family:"Lora",serif;font-style:italic;font-size:11px;line-height:1.35}
  .back-warning{position:absolute;left:18px;top:182px;width:262px;border:1px solid var(--ink);padding:4px 6px;font-family:"Arimo",sans-serif;font-size:9px;line-height:1.3}
  .back-ingredients{position:absolute;left:18px;top:264px;width:262px;font-family:"Arimo",sans-serif;font-size:9px;line-height:1.3}
  .back-producer{position:absolute;left:18px;top:320px;font-family:"Arimo",sans-serif;font-size:10px;line-height:1.3}
  .back-recycle{position:absolute;left:124px;top:352px}
  .back-barcode-slot{position:absolute;left:170px;top:340px;width:108px;height:58px;border:1px solid var(--dim);display:flex;align-items:center;justify-content:center;font-family:"Arimo",sans-serif;font-size:10px}
  strong{font-weight:700}
</style>
</head>
<body>
<div class="canvas">

  <div class="dimension" style="left:76px;top:96px">
    <svg width="549" height="20"><line x1="0" y1="10" x2="549" y2="10" stroke="#8a8a8a"/><line x1="0" y1="2" x2="0" y2="18" stroke="#8a8a8a"/><line x1="549" y1="2" x2="549" y2="18" stroke="#8a8a8a"/></svg>
    <span class="dimension-label" style="left:250px;top:-14px">150 mm</span>
  </div>
  <div class="dimension" style="left:650px;top:150px">
    <svg width="20" height="510"><line x1="10" y1="0" x2="10" y2="510" stroke="#8a8a8a"/><line x1="2" y1="0" x2="18" y2="0" stroke="#8a8a8a"/><line x1="2" y1="510" x2="18" y2="510" stroke="#8a8a8a"/></svg>
    <span class="dimension-label" style="left:-8px;top:240px;transform:rotate(90deg)">165 mm</span>
  </div>

  <section class="label label-front">
    <div class="art-rose-main" role="img" aria-label="Illustration of pink garden roses with green leaves"></div>
    <div class="art-rose-side" role="img" aria-label="Illustration of a pink rose with buds"></div>
    <div class="art-leaves-base" role="img" aria-label="Illustration of green leaves"></div>
    <div class="front-title line-1">Hollow</div>
    <div class="front-title line-2">Lantern</div>
    <div class="front-badge" role="img" aria-label="Handcrafted seal"></div>
    <div class="front-batch">SMALL BATCH</div>
    <div class="front-drink">My Drink Name</div>
    <div class="front-rule"></div>
    <div class="front-specs"><span>% ALC/VOL</span><span class="volume">700ML</span><span>BATCH NO</span></div>
  </section>

  <div class="dimension" style="left:185px;top:724px">
    <svg width="294" height="20"><line x1="0" y1="10" x2="294" y2="10" stroke="#8a8a8a"/><line x1="0" y1="2" x2="0" y2="18" stroke="#8a8a8a"/><line x1="294" y1="2" x2="294" y2="18" stroke="#8a8a8a"/></svg>
    <span class="dimension-label" style="left:126px;top:-14px">90 mm</span>
  </div>
  <div class="dimension" style="left:504px;top:770px">
    <svg width="20" height="420"><line x1="10" y1="0" x2="10" y2="420" stroke="#8a8a8a"/><line x1="2" y1="0" x2="18" y2="0" stroke="#8a8a8a"/><line x1="2" y1="420" x2="18" y2="420" stroke="#8a8a8a"/></svg>
    <span class="dimension-label" style="left:-6px;top:200px;transform:rotate(90deg)">120 mm</span>
  </div>

  <section class="label label-back">
    <div class="back-title">Hollow Lantern</div>
    <div class="art-rose-back" role="img" aria-label="Illustration of a pink rose sprig"></div>
    <p class="back-description">Lorem ipsum dolor sit amet, consectetuer adipiscing elit, sed diam nonummy nibh euismod tincidunt ut laoreet dolore magna aliquam erat volutpat. Ut wisi enim ad minim veniam, quis nostrud exerci tation ullamcorper suscipit lobortis nisl ut aliquip ex ea commodo consequat.</p>
    <p class="back-warning"><strong>GOVERNMENT WARNING:</strong> Lorem ipsum dolor sit amet, consectetuer adipiscing elit, sed diam nonummy nibh euismod tincidunt ut laoreet dolore magna aliquam erat volutpat. Ut wisi enim ad minim veniam, quis nostrud exerci tation ullamcorper suscipit lobortis nisl ut aliquip ex ea commodo consequat, dolore te feugait nulla facilisi.</p>
    <p class="back-ingredients"><strong>INGREDIENTS:</strong> Lorem ipsum dolor sit amet, consectetuer adipiscing elit, sed diam nonummy nibh euismod tincidunt ut laoreet dolore magna aliquam erat volutpat.</p>
    <p class="back-producer"><strong>PRODUCER</strong><br>Company<br>Address<br>Phone<br>www.company.com</p>
    <svg class="back-recycle" width="34" height="32" viewBox="0 0 34 32" role="img" aria-label="Recycle icon">
      <g fill="none" stroke="#8a8a8a" stroke-width="2" stroke-linecap="round" stroke-linejoin="round">
        <path d="M13 5 L17 2 L21 8"/>
        <path d="M21 8 L19 4 M21 8 L16.5 8.5"/>
        <path d="M26 14 L31 24 L24 28"/>
        <path d="M24 28 L27 25 M24 28 L27 31"/>
        <path d="M15 28 L3 28 L8 19"/>
        <path d="M8 19 L9 23.5 M8 19 L4 21"/>
      </g>
    </svg>
    <div class="back-barcode-slot">BARCODE</div>
  </section>

</div>
</body>
</html>
```